Folk figures playing cards design

I need design of playing cards with polish folk characters from Kurpie region. I expect to get 4 designs for card number 6, J,
Q and K. In attached files I am sending example of folk outfits for J, Q and K cards. For J man should not have a hat. Design
of the back side of card is also expected - the best is to use as inspiration traditional cutouts from Kurpie available under
www.zbiory.lesnodolskie.pl or findora search: "wycinanki kurpiowskie"

Target Market(s)

people living in Kurpie region - age 20-35

Font styles to use
Serif
Decorative

Requirements
Must have
• Figures on cards should wear traditional clothes presented on pictures. Colors of the clothes should stay the same. Red should be red, but it can be a bit darker or broghter
Should not have
• naked content

```html
<!DOCTYPE html>
<html lang="pl">
<head>
<meta charset="utf-8">
<title>Szóstka kier</title>
<link rel="stylesheet" href="https://fonts.googleapis.com/css2?family=Playfair+Display:wght@700&display=swap">
<style>
  :root {
    --page: #ffffff;
    --card-face: #ddd7b9;
    --suit-red: #b51306;
    --frame-red: #b8140a;
    --ink: #1a0d0b;
  }
  html, body {
    margin: 0;
    padding: 0;
    width: 848px;
    height: 1200px;
    overflow: hidden;
    background: var(--page);
  }
  .playing-card {
    display: block;
    width: 848px;
    height: 1200px;
  }
  .card-face { fill: var(--card-face); }
  .frame-bar {
    fill: var(--frame-red);
    stroke: var(--ink);
    stroke-width: 1.5;
  }
  .heart-pip {
    fill: var(--suit-red);
    stroke: var(--ink);
    stroke-width: 3;
    stroke-linejoin: round;
  }
  .corner-index {
    font-family: "Playfair Display", serif;
    font-weight: 700;
    font-size: 104px;
    fill: var(--frame-red);
    stroke: var(--ink);
    stroke-width: 1.5;
    text-anchor: middle;
  }
</style>
</head>
<body>
<svg class="playing-card" viewBox="0 0 768 1087" preserveAspectRatio="none" role="img" aria-label="Szóstka kier">
  <defs>
    <path id="heart" class="heart-pip"
      d="M0,-38 C-18,-78 -70,-74 -70,-28 C-70,14 -22,42 0,72 C22,42 70,14 70,-28 C70,-74 18,-78 0,-38 Z"/>
  </defs>

  <rect class="card-face" x="62" y="45" width="650" height="958"/>

  <g class="card-frame">
    <rect class="frame-bar" x="78" y="34" width="660" height="18" rx="4"/>
    <rect class="frame-bar" x="50" y="150" width="20" height="850" rx="4"/>
    <rect class="frame-bar" x="60" y="996" width="600" height="20" rx="4"/>
    <rect class="frame-bar" x="680" y="58" width="20" height="862" rx="4"/>
  </g>

  <text class="corner-index" x="62" y="126">6</text>
  <g transform="translate(700 992) rotate(180)">
    <text class="corner-index" x="0" y="36">6</text>
  </g>

  <g class="pips">
    <use href="#heart" x="215" y="155"/>
    <use href="#heart" x="550" y="155"/>
    <use href="#heart" x="375" y="385"/>
    <use href="#heart" transform="translate(385 637) rotate(180)"/>
    <use href="#heart" transform="translate(210 880) rotate(180)"/>
    <use href="#heart" transform="translate(545 880) rotate(180)"/>
  </g>
</svg>
</body>
</html>
```